Velmint website

A clean uncluttered design that shows at glance that we are in the Media and design and publishing business.

We would like to see designs that use colours that show warmth and quality.

The website should show:
- products
- projects

These should be displaxed in spaces that we can add or interchanges with new products or projects.
Updates

Target Market(s)

Business and project managers and buyers and authors.

Industry/Entity Type

Business

Requirements
Must have
• Good colours. Not too strong, not weak, but reflecting quality.

```html
<!DOCTYPE html>
<html lang="en">
<head>
<meta charset="utf-8">
<title>Velmint Media</title>
<link rel="stylesheet" href="https://fonts.googleapis.com/css2?family=Oswald:wght@300;400&family=Open+Sans:wght@400;600;700&family=Great+Vibes&display=swap">
<style>
:root{
  --green:#5c8300;
  --green-dark:#4f7200;
  --white:#ffffff;
  --ink:#111111;
  --cyan:#2ec3f0;
  --slate:#2a2a2a;
  --red:#d90c0c;
  --gray:#6b6b6b;
  --social-a:#3b5a9a;
  --social-b:#29c2ef;
}
*{margin:0;padding:0;box-sizing:border-box}
html,body{width:1200px;height:1198px;overflow:hidden;background:var(--white)}
body{position:relative;font-family:"Open Sans",sans-serif;color:var(--ink)}
.abs{position:absolute}
.logo{left:87px;top:16px;font-family:"Open Sans",sans-serif;font-weight:700;font-size:27px;line-height:25px;text-align:center;letter-spacing:0.5px}
.nav{left:0;top:14px;width:1200px;height:46px}
.nav a{position:absolute;top:0;height:46px;line-height:46px;font-family:"Oswald",sans-serif;font-weight:300;font-size:22px;color:var(--ink);text-decoration:none;letter-spacing:-0.5px}
.nav a.active{background:var(--green);color:var(--white);padding:0 10px}
.hero{left:88px;top:74px;width:1023px;height:487px;background:linear-gradient(160deg,#c9ccd1 0%,#8a8f98 35%,#4b4a4f 65%,#6b4b45 100%)}
.hero-fade{left:1111px;top:74px;width:89px;height:487px;background:linear-gradient(90deg,#e8e8e8,#f8f8f8)}
.arrow{width:40px;height:40px;border-radius:50%;background:#b8b8b8}
.slogan{left:88px;top:364px;width:1023px;text-align:center;font-family:"Great Vibes",cursive;font-size:38px;color:var(--white);font-weight:400}
.sub{left:88px;top:410px;width:1023px;text-align:center;font-size:13px;color:var(--white)}
.btn{top:471px;height:48px;display:flex;align-items:center;font-family:"Oswald",sans-serif;font-weight:300;font-size:22px;color:var(--white);letter-spacing:-0.5px}
.btn .box{position:absolute;right:20px;top:12px;width:28px;height:26px;background:var(--white)}
.btn-cat{left:330px;width:273px;background:var(--cyan);padding-left:25px}
.btn-news{left:603px;width:274px;background:var(--slate);padding-left:25px}
.band{left:0;top:561px;width:1200px;height:637px;background:var(--green)}
.sec-title{left:0;top:594px;width:1200px;text-align:center;font-family:"Oswald",sans-serif;font-weight:300;font-size:22px;color:var(--white);letter-spacing:-0.5px}
.sec-title span{display:inline-flex;align-items:center;gap:0}
.sec-title i{display:inline-block;width:56px;height:2px;background:var(--white)}
.prod{top:650px;width:160px}
.prod .ph{width:160px;height:142px}
.prod h3{margin-top:8px;text-align:center;font-weight:600;font-size:15px;color:var(--white);white-space:nowrap}
.prod p{text-align:center;font-size:10px;font-weight:600;color:var(--white);margin-top:2px}
.card{top:871px;width:296px;height:240px;background:var(--white)}
.card h2{position:absolute;left:21px;top:32px;font-family:"Oswald",sans-serif;font-weight:300;font-size:26px;display:flex;align-items:center;gap:6px;letter-spacing:-0.5px}
.card .ph{position:absolute;left:21px;top:78px;width:130px;height:130px}
.card p{position:absolute;left:161px;top:86px;width:130px;font-size:13.5px;line-height:15.5px}
.card .more{position:absolute;top:221px;height:20px;width:87px;background:var(--red);color:var(--white);font-size:13px;line-height:20px;text-align:center}
.contact{left:178px;top:1081px;font-size:10px;font-weight:600;color:var(--gray);white-space:nowrap}
.foot{left:222px;top:1152px;font-family:"Oswald",sans-serif;font-weight:300;font-size:16px;color:var(--white);white-space:nowrap;letter-spacing:-0.5px}
.pin{left:143px;top:1149px}
.social{top:1149px;height:20px;line-height:20px;font-size:12px;font-weight:600;color:var(--white);text-align:center}
</style>
</head>
<body>
<div class="abs logo">VELMINT<br>MEDIA</div>
<nav class="abs nav">
  <a style="left:496px">HOME</a>
  <a class="active" style="left:566px;width:103px;text-align:center">ABOUT US</a>
  <a style="left:700px">PRODUCTS</a>
  <a style="left:815px">PROJECTS</a>
  <a style="left:931px">BLOGS</a>
  <a style="left:1023px">CONTACT US</a>
</nav>

<div class="abs hero" role="img" aria-label="Photo of a press conference with journalists holding microphones and a camera toward a speaker"></div>
<div class="abs hero-fade"></div>
<svg class="abs arrow" style="left:32px;top:275px" viewBox="0 0 40 40"><circle cx="20" cy="20" r="20" fill="#b8b8b8"/><path d="M23 12 L15 20 L23 28" stroke="#fff" stroke-width="4" fill="none"/></svg>
<svg class="abs arrow" style="left:1128px;top:275px" viewBox="0 0 40 40"><circle cx="20" cy="20" r="20" fill="#b8b8b8"/><path d="M17 12 L25 20 L17 28" stroke="#fff" stroke-width="4" fill="none"/></svg>
<div class="abs slogan">Velmint Media Lorem Ipsum - Dummy Slogan, Labore Magna Aliqua</div>
<div class="abs sub">Lorem ipsum dolor sit amet, consectetur adipisicing elit, sed do eiusmod tempor incididunt ut labore et dolore magna aliqua.</div>
<div class="abs btn btn-cat">OUR PRODUCT CATALOUES<svg class="box" viewBox="0 0 28 26"><rect width="28" height="26" fill="#fff"/><path d="M8 13h8M13 9l5 4-5 4" stroke="#000" stroke-width="3" fill="none"/></svg></div>
<div class="abs btn btn-news">SUBSCRIBE NEWSLETTER<svg class="box" viewBox="0 0 28 26"><rect width="28" height="26" fill="#fff"/><path d="M8 13h8M13 9l5 4-5 4" stroke="#000" stroke-width="3" fill="none"/></svg></div>

<div class="abs band"></div>
<div class="abs sec-title"><span><i></i>OUR PRODUCTS<i></i></span></div>

<div class="abs prod" style="left:144px"><div class="ph" role="img" aria-label="Hands operating a video camera" style="background:linear-gradient(135deg,#5d6b4a,#2b2f33 55%,#4a6aa0)"></div><h3>Lorem Ipsum Product</h3><p>&#9906; ZOOM</p></div>
<div class="abs prod" style="left:331px"><div class="ph" role="img" aria-label="Hand holding a mobile phone" style="background:linear-gradient(135deg,#d8d8d8,#7d7d80 50%,#c49a86)"></div><h3>Lorem Ipsum Product</h3><p>&#9906; ZOOM</p></div>
<div class="abs prod" style="left:518px"><div class="ph" role="img" aria-label="Camera monitor screen showing a scene" style="background:linear-gradient(135deg,#8a1010,#1b1b1b 50%,#9bb86a)"></div><h3>Lorem Ipsum Product</h3><p>&#9906; ZOOM</p></div>
<div class="abs prod" style="left:705px"><div class="ph" role="img" aria-label="Hand holding a mobile phone" style="background:linear-gradient(135deg,#d8d8d8,#7d7d80 50%,#c49a86)"></div><h3>Lorem Ipsum Product</h3><p>&#9906; ZOOM</p></div>
<div class="abs prod" style="left:893px"><div class="ph" role="img" aria-label="Hands operating a video camera" style="background:linear-gradient(135deg,#5d6b4a,#2b2f33 55%,#4a6aa0)"></div><h3>Lorem Ipsum Product</h3><p>&#9906; ZOOM</p></div>

<div class="abs card" style="left:144px">
  <h2><svg width="20" height="20" viewBox="0 0 20 20"><rect width="20" height="20" rx="3" fill="#111"/><circle cx="10" cy="10" r="4" fill="#fff"/></svg>What we do?</h2>
  <div class="ph" role="img" aria-label="Hand using a phone beside a laptop" style="background:linear-gradient(135deg,#cfd6da,#e9ecee 50%,#b78c7a)"></div>
  <p>Excepteur sint occaecat cupidatat non proident, sunt in culpa qui officia deserunt mollit anim id est laborum.</p>
  <div class="more" style="left:165px">Learn More</div>
</div>
<div class="abs contact">PHONE : +01 40 55 18 62 - &nbsp;EMAIL : INFO@VELMINTMEDIA.CO</div>
<div class="abs card" style="left:453px">
  <h2><svg width="20" height="20" viewBox="0 0 20 20"><rect width="20" height="20" rx="3" fill="#111"/><circle cx="10" cy="10" r="4" fill="#fff"/></svg>Our Projects</h2>
  <div class="ph" role="img" aria-label="Person listening with white headphones" style="background:linear-gradient(135deg,#6e8aa6,#b39373 55%,#e7e1da)"></div>
  <p>Excepteur sint occaecat cupidatat non proident, sunt in culpa qui officia deserunt mollit anim id est laborum.</p>
  <div class="more" style="left:166px">Learn More</div>
</div>
<div class="abs card" style="left:760px">
  <h2><svg width="20" height="20" viewBox="0 0 20 20"><rect width="20" height="20" rx="3" fill="#111"/><circle cx="10" cy="10" r="4" fill="#fff"/></svg>For Professionals</h2>
  <div class="ph" role="img" aria-label="Businessman holding a laptop in an office" style="background:linear-gradient(135deg,#dfe6ea,#9fb4c4 50%,#5a7fa8)"></div>
  <p>Excepteur sint occaecat cupidatat non proident, sunt in culpa qui officia deserunt mollit anim id est laborum.</p>
  <div class="more" style="left:165px">Learn More</div>
</div>

<svg class="abs pin" width="26" height="36" viewBox="0 0 26 36"><path d="M13 0C5.8 0 0 5.6 0 12.6 0 22 13 36 13 36s13-14 13-23.4C26 5.6 20.2 0 13 0z" fill="#fff"/><circle cx="13" cy="12.5" r="5" fill="var(--green)"/></svg>
<div class="abs foot">HOME - ABOUT US - PRODUCT - BLOGS- FAQS - CONTACT - LOCATION</div>
<div class="abs social" style="left:931px;width:73px;background:var(--social-a)">Friendly</div>
<div class="abs social" style="left:1004px;width:52px;background:var(--social-b)">chirper</div>
</body>
</html>
```